Book cover design : The Hollow Bell

We need a striking book cover design for a book which will be published via Larkspur Reader and as a paperback. The book is a simple short story - ghost story - for children. The book is set in a contemporary English town.

The title of the book is : The Hollow Bell
The author is: Rupert Clowe

The book is a story book, for children, aged approximately 11-15 years old.
It is a ghost story, but not too scary.

Text to go on the front cover:
The Hollow Bell

Rupert Clowe

Text to go on the back cover :

The Hollow Bell; a ghost story of controlled readability for students aged 11 to 15 years, (catch-up reading). Also for students of English as a foreign language.

Target Market(s)

A ghost story of controlled readability for students aged 11 to 15 years, (catch-up reading). Also for students of English as a foreign language.

```html
<!DOCTYPE html>
<html lang="en">
<head>
<meta charset="utf-8">
<title>The Hollow Bell — Rupert Clowe — Cover Spread</title>
<link rel="stylesheet" href="https://fonts.googleapis.com/css2?family=Bebas+Neue&family=Crimson+Pro:wght@400&family=Rubik+Dirt&display=swap">
<style>
  :root {
    --page: #ffffff;
    --ink: #050505;
    --author-white: #ffffff;
    --title-yellow: #fbf383;
    --title-grey: #cbcbcb;
    --blurb-white: #f4f4f4;
    --teal-deep: #0b1615;
    --teal-mid: #2f5a58;
    --teal-light: #8fc2bf;
  }
  * { margin: 0; padding: 0; box-sizing: border-box; }
  html, body {
    width: 1200px;
    height: 964px;
    overflow: hidden;
    background: var(--page);
  }
  .spread {
    position: relative;
    width: 1200px;
    height: 964px;
  }
  .cover {
    position: absolute;
    top: 47px;
    width: 543px;
    height: 871px;
    overflow: hidden;
    background: var(--ink);
  }
  .cover--back { left: 47px; }
  .cover--front { left: 611px; }

  .cover-art {
    position: absolute;
    inset: 0;
    background:
      radial-gradient(ellipse 45% 60% at 68% 62%, var(--teal-light) 0%, var(--teal-mid) 38%, rgba(11,22,21,0) 75%),
      radial-gradient(ellipse 60% 70% at 60% 40%, #1c302f 0%, var(--teal-deep) 60%, var(--ink) 100%);
  }
  .cover-art--faint {
    background: radial-gradient(ellipse 60% 70% at 60% 55%, #141414 0%, var(--ink) 80%);
  }

  .author {
    position: absolute;
    left: 0;
    right: 0;
    text-align: center;
    font-family: "Bebas Neue", "Oswald", sans-serif;
    color: var(--author-white);
    line-height: 1;
    white-space: nowrap;
    transform-origin: center top;
  }
  .cover--back .author { top: 40px; font-size: 91px; transform: scaleX(0.78); }
  .cover--front .author { top: 33px; font-size: 137px; transform: scaleX(0.74); }

  .title {
    font-family: "Rubik Dirt", "Impact", sans-serif;
    font-weight: 400;
  }
  .title-line {
    position: absolute;
    display: block;
    line-height: 1;
    white-space: nowrap;
  }
  .title-line--the { color: var(--title-yellow); transform-origin: left top; }
  .title-line--hollow { color: var(--title-grey); transform-origin: right top; }
  .title-line--bell { color: var(--title-grey); transform-origin: left top; }

  .cover--back .title-line--the { left: 136px; top: 133px; font-size: 134px; transform: scaleX(0.45); }
  .cover--back .title-line--hollow { right: 128px; top: 235px; font-size: 122px; transform: scaleX(0.44); }
  .cover--back .title-line--bell { left: 136px; top: 332px; font-size: 174px; transform: scaleX(0.51); }

  .cover--front .title-line--the { left: 23px; top: 171px; font-size: 140px; transform: scaleX(0.465); }
  .cover--front .title-line--hollow { right: 226px; top: 279px; font-size: 124px; transform: scaleX(0.45); }
  .cover--front .title-line--bell { left: 23px; top: 384px; font-size: 184px; transform: scaleX(0.51); }

  .blurb {
    position: absolute;
    left: 0;
    right: 0;
    top: 530px;
    text-align: center;
    font-family: "Crimson Pro", "Minion Pro", serif;
    font-size: 38px;
    line-height: 50px;
    letter-spacing: 0.8px;
    color: var(--blurb-white);
    white-space: nowrap;
  }
</style>
</head>
<body>
<main class="spread">

  <section class="cover cover--back" aria-label="Back cover">
    <div class="cover-art cover-art--faint" role="img" aria-label="Faint dark image of a woman in a Victorian gown standing in an arched doorway"></div>
    <p class="author">Rupert Clowe</p>
    <h2 class="title">
      <span class="title-line title-line--the">THE</span>
      <span class="title-line title-line--hollow">HOLLOW</span>
      <span class="title-line title-line--bell">BELL</span>
    </h2>
    <p class="blurb">The Hollow Bell; a ghost story<br>of controlled readability<br>for students aged 11 to 15 years,<br>(catch-up reading).<br>Also for students of<br>English as a foreign language.</p>
  </section>

  <section class="cover cover--front" aria-label="Front cover">
    <div class="cover-art" role="img" aria-label="Illustration of a ghostly woman in a pale teal Victorian gown standing in a dark arched stone doorway"></div>
    <p class="author">Rupert Clowe</p>
    <h1 class="title">
      <span class="title-line title-line--the">THE</span>
      <span class="title-line title-line--hollow">HOLLOW</span>
      <span class="title-line title-line--bell">BELL</span>
    </h1>
  </section>

</main>
</body>
</html>
```